Book Cover for Memoir: Sexual Assault and Traumatic Stress

I need a cover design for a memoir that is a victim's story of a sexual assault. I will need a print-on-demand cover, an eBook cover, and a 3D thumbnail image. The thumbnail and eBook cover will be used immediately, and the POD cover will be used in a few months with the full manuscript is ready. Therefore, I need an artist who is willing to make small adjustments if needed once the page count is set.

I have a image I have purchased that should give you an idea of the desired direction, but you can feel free to use your own images. I have attached some examples of book covers I like. I attached a color palette for fonts.

Overall Look: Fonts should be feminine and thin, but large to stand out. Look should be simple and elegant, and display and overall depressing feeling. There should be enough detail though to make it look professionally put together. Not TOO minimalistic.

I have also attached the Print Harbor templates if you choose to use those. If not, ensure there is an open place for the barcode on the bottom right.

Requirements
Must have
• Title: Beneath Quiet Rain
Subtitle: One Woman's Account of Fear, Guilt & Silence
Author: Dana Ruth Whitford
Audience: Mostly women 18-30
Quote (for the back): "I always thought I'd know how I'd react if I ever was raped. I was wrong. I've been wrong a lot lately."
Summary (back cover): When twenty-seven-year-old Dana Whitford wakes up with a gut-wrenching feeling, she has little memory of the horrifying events that occurred the night before. Days earlier, Dana was a spirited single mom who had abandoned her hometown to raise her daughter in the city and pursue her dreams. In the short months since Dana’s move to Seattle, she became the adored lover of a charismatic lawyer, started a new business, and finally felt life was going her way. So what happened to cause her to break?

In a gripping and heartbreaking narrative, Dana tells the true story of how her life unraveled from the traumatic events that took place that night and why what seems obvious to everyone else is impossible for Dana to believe. Beneath Quiet Rain is a chilling exploration of memory through trauma, trust in humanity, and a captivating story of strength and survival that appeals to the heart of fathers and mothers, sons and daughters, and men and women alike.
Nice to have
• BACK COVER: I'd like to have a photo on the back. This should depict the happy life of the main character before the sexual assault, and should be with her daughter. Or should be a nature scene that starts at the corner and blends into the rest of the cover. I have attached a possible image or you can use something you like.

```html
<!DOCTYPE html>
<html lang="en">
<head>
<meta charset="utf-8">
<title>Beneath Quiet Rain – Cover</title>
<link rel="stylesheet" href="https://fonts.googleapis.com/css2?family=Big+Shoulders+Display:wght@200;300&family=Oswald:wght@400&family=Cormorant+SC:wght@500&family=Didact+Gothic&family=Open+Sans:wght@400&display=swap">
<style>
  :root {
    --spine-blue: #1f3687;
    --back-blue: #213a8c;
    --aqua: #52ecc4;
    --ink-dark: #3a3a3e;
    --white: #ffffff;
    --shadow: rgba(0,0,0,0.55);
  }
  * { margin: 0; padding: 0; box-sizing: border-box; }
  html, body { width: 1200px; height: 841px; overflow: hidden; background: #fff; }
  .cover { position: relative; width: 1200px; height: 841px; overflow: hidden; }

  /* Back cover */
  .back { position: absolute; left: 0; top: 0; width: 560px; height: 841px; background: var(--back-blue); }
  .back-photo {
    position: absolute; left: 0; top: 0; width: 560px; height: 415px;
    background:
      radial-gradient(ellipse 220px 160px at 430px 80px, rgba(255,246,215,0.95), rgba(255,230,180,0) 70%),
      linear-gradient(180deg, #c9d6df 0%, #e8dcc4 38%, #b6b3a6 55%, #3d6f86 60%, #5a8ea0 68%, #cfc7b6 78%, #d8cbb4 100%);
  }
  .back-quote {
    position: absolute; left: 40px; top: 50px; width: 340px;
    font-family: "Cormorant SC", serif; font-weight: 500;
    font-size: 21px; line-height: 32px; color: #1b1b20;
  }
  .back-quote .mark { color: var(--aqua); font-size: 26px; }
  .blurb {
    position: absolute; left: 52px; top: 433px; width: 456px;
    font-family: "Open Sans", sans-serif; font-size: 8.4px; line-height: 21px;
    color: var(--white); text-align: center;
  }
  .blurb p + p { margin-top: 21px; }
  .blurb .initial { color: var(--aqua); font-size: 11px; }
  .barcode-space { position: absolute; left: 350px; top: 707px; width: 187px; height: 110px; background: var(--white); }

  /* Spine */
  .spine { position: absolute; left: 560px; top: 0; width: 80px; height: 841px; background: var(--spine-blue); }
  .spine-line {
    position: absolute; left: 40px; top: 0;
    transform-origin: 0 0; transform: rotate(90deg) translateY(-50%);
    white-space: nowrap; display: flex; align-items: center;
  }
  .spine-title { font-family: "Big Shoulders Display", sans-serif; font-weight: 300; font-size: 46px; color: var(--aqua); letter-spacing: 1px; margin-left: 30px; }
  .spine-subtitle { font-family: "Oswald", sans-serif; font-size: 17px; line-height: 19px; color: var(--white); margin-left: 14px; }
  .spine-author { font-family: "Didact Gothic", sans-serif; font-size: 27px; color: var(--aqua); position: absolute; left: 610px; }

  /* Front cover */
  .front { position: absolute; left: 640px; top: 0; width: 560px; height: 841px; }
  .front-photo {
    position: absolute; inset: 0;
    background:
      radial-gradient(ellipse 260px 200px at 430px 760px, rgba(30,30,70,0.9), rgba(30,30,70,0) 75%),
      radial-gradient(ellipse 300px 260px at 220px 120px, rgba(240,210,215,0.85), rgba(240,210,215,0) 70%),
      linear-gradient(160deg, #e9d3d6 0%, #d5cbc6 35%, #9fb6a6 60%, #6f8f86 80%, #3f4f5e 100%);
  }
  .author {
    position: absolute; left: 165px; top: 28px;
    font-family: "Didact Gothic", sans-serif; font-size: 29px; color: var(--ink-dark);
  }
  .title {
    position: absolute; left: 0; top: 0; width: 560px; height: 430px;
    font-family: "Big Shoulders Display", sans-serif; font-weight: 200;
    color: var(--aqua); text-shadow: 1px 2px 3px rgba(0,0,0,0.35); line-height: 1;
  }
  .title span { position: absolute; font-size: 96px; letter-spacing: -1px; }
  .title .w1 { left: 48px; top: 146px; }
  .title .w2 { left: 190px; top: 232px; }
  .title .w3 { left: 382px; top: 314px; }
  .subtitle {
    position: absolute; right: 174px; top: 356px; text-align: right;
    font-family: "Oswald", sans-serif; color: var(--white);
    text-shadow: 1px 1px 3px var(--shadow);
  }
  .subtitle .lead { display: block; font-size: 17px; line-height: 22px; }
  .subtitle .main { display: block; font-size: 22px; line-height: 28px; }
</style>
</head>
<body>
<main class="cover">
  <section class="back">
    <div class="back-photo" role="img" aria-label="Sunset beach scene with a mother and young daughter in blue dresses walking hand in hand by the waves"></div>
    <blockquote class="back-quote"><span class="mark">“</span>I always thought I'd know how I'd react if I ever was raped. I was wrong. I've been wrong a lot lately.<span class="mark">”</span></blockquote>
    <div class="blurb">
      <p><span class="initial">W</span>hen twenty-seven-year-old Dana Whitford wakes up with a gut-wrenching feeling, she has little memory of the horrifying events that occurred the night before. Days earlier, Dana was a spirited single mom who had abandoned her hometown to raise her daughter in the city and pursue her dreams. In the short months since Dana’s move to Seattle, she became the adored lover of a charismatic lawyer, started a new business, and finally felt life was going her way. So what happened to cause her to break?</p>
      <p><span class="initial">I</span>n a gripping and heartbreaking narrative, Dana tells the true story of how her life unraveled from the traumatic events that took place that night and why what seems obvious to everyone else is impossible for Dana to believe. Beneath Quiet Rain is a chilling exploration of memory through trauma, trust in humanity, and a captivating story of strength and survival that appeals to the heart of fathers and mothers, sons and daughters, and men and women alike.</p>
    </div>
    <div class="barcode-space"></div>
  </section>

  <section class="spine">
    <div class="spine-line">
      <span class="spine-title">BENEATH QUIET RAIN</span>
      <span class="spine-subtitle">One Woman's Account of<br>Fear, Guilt &amp; Silence</span>
      <span class="spine-author">Dana Ruth Whitford</span>
    </div>
  </section>

  <section class="front">
    <div class="front-photo" role="img" aria-label="Young woman with dark hair lying back in pale water, wearing a pearl bracelet, soft pink and green tones"></div>
    <p class="author">Dana Ruth Whitford</p>
    <h1 class="title"><span class="w1">BENEATH</span><span class="w2">QUIET</span><span class="w3">RAIN</span></h1>
    <p class="subtitle"><span class="lead">One Woman's Account of</span><span class="main">Fear, Guilt &amp; Silence</span></p>
  </section>
</main>
</body>
</html>
```